business card for WRT pty ltd

We require a business card that stands out . I have included our company flyer and would like the services listed to be put on the card so when we Give out the cards to customers they have an idea of services we provide. need the winning design to be in editable photo shop format, editable iMac pages format or editable windows publisher format, so that I can enter in names, email addresses, phone numbers etc myself. I have included a pdf documents of info / items needed on the card to use as reference please.
Updates

need more submissions

Need extra days to review

Sick

Target Market(s)

new customers

Contact Information for Business Card

details are on attached business card requirements file

Requirements
Must have
• I have attached a list of must haves

```html
<!DOCTYPE html>
<html lang="en">
<head>
<meta charset="utf-8">
<title>WRT pty ltd – Business Card</title>
<link href="https://fonts.googleapis.com/css2?family=Audiowide&family=Lato:wght@400;700;900&family=Montserrat:wght@500;800&display=swap" rel="stylesheet">
<style>
:root{
  --page:#2b2b2b;
  --card:#0b0b0b;
  --card-edge:#161616;
  --red:#e8232a;
  --white:#ffffff;
  --silver:#b9b9b9;
  --sand-1:#3a2a20;
  --sand-2:#a5704f;
  --sand-3:#c99a7a;
}
*{box-sizing:border-box;margin:0;padding:0}
html,body{width:1200px;height:1080px;overflow:hidden;background:var(--page)}
body{position:relative;font-family:"Lato",sans-serif;color:var(--white)}

.card{
  position:absolute;left:254px;width:693px;height:426px;
  border-radius:20px;overflow:hidden;
  background:radial-gradient(ellipse at 50% 40%,var(--card-edge) 0%,var(--card) 70%);
}
.card--front{top:93px}
.card--back{top:558px}

/* front */
.brand-name{
  position:absolute;left:0;right:0;text-align:center;
  font-family:"Montserrat",sans-serif;font-weight:800;color:var(--silver);
  letter-spacing:4px;line-height:1;
}
.card--front .brand-name{top:38px;font-size:64px}

.fleet-photo{
  position:absolute;left:0;top:130px;width:100%;height:122px;
  background:linear-gradient(180deg,var(--card) 0%,var(--sand-1) 45%,var(--sand-2) 75%,var(--sand-3) 100%);
}
.services-tab{position:absolute;left:0;top:217px;width:693px;height:39px}
.services-tab__label{
  position:absolute;right:27px;top:223px;
  font-family:"Audiowide",sans-serif;font-size:20px;color:var(--white);letter-spacing:.5px;
}

.services{position:absolute;top:264px;list-style:none;font-family:"Montserrat",sans-serif;font-weight:500;font-size:17px}
.services li{height:24.6px;line-height:24.6px;white-space:nowrap}
.services li::before,.services li::after{color:var(--red);font-size:13px;vertical-align:1px}
.services--left{left:24px}
.services--left li::before{content:"●";margin-right:7px}
.services--right{right:26px;text-align:right}
.services--right li::after{content:"●";margin-left:7px}

.quote-note{
  position:absolute;left:312px;top:300px;width:170px;
  transform:rotate(-30deg);transform-origin:center;
  font-family:"Lato",sans-serif;font-size:10px;line-height:1.25;
  color:var(--red);text-align:center;
}

/* back */
.card--back .brand-name{left:42px;right:auto;width:280px;top:178px;font-size:72px}
.divider{position:absolute;left:345px;top:136px;width:2px;height:157px;background:var(--red)}
.contact{position:absolute;left:366px;top:134px}
.contact__name{font-weight:900;font-size:29px;color:var(--red);line-height:1}
.contact__role{font-size:18px;font-weight:700;margin-top:8px}
.contact__list{list-style:none;margin-top:15px}
.contact__list li{display:flex;align-items:center;gap:8px;font-size:18.5px;height:27px}
.contact__list svg{width:16px;height:16px;flex:none}
.depot{position:absolute;left:0;right:0;top:356px;text-align:center;font-size:18px}
.depot__label{color:var(--red)}
</style>
</head>
<body>

<section class="card card--front">
  <div class="brand-name">WRT</div>
  <div class="fleet-photo" role="img" aria-label="Photo of a black road train truck with three tipper trailers on red outback dirt"></div>

  <svg class="services-tab" viewBox="0 0 693 39" aria-hidden="true">
    <polygon points="416,35 446,0 693,0 693,35" fill="var(--red)"/>
    <rect x="0" y="35" width="693" height="4" fill="var(--red)"/>
  </svg>
  <div class="services-tab__label">OUR SERVICES</div>

  <ul class="services services--left">
    <li>Over size loads/Hot Shot Loads</li>
    <li>Heavy Vehicle Recovery services</li>
    <li>Portable Water Deliveries</li>
    <li>Road Building / Maintenance</li>
    <li>Earthworks</li>
    <li>Sand &amp; Metal Supply &amp; Cartage</li>
  </ul>

  <p class="quote-note">we offer a large range of services not listed so call us today for a personalized quote to suit your needs.</p>

  <ul class="services services--right">
    <li>Raod train Tippers</li>
    <li>Road Train Tankers</li>
    <li>Road Train Flat Tops</li>
    <li>Drop Deck Trailers</li>
    <li>Mine Site Accredited</li>
    <li>Equipment &amp; Operators</li>
  </ul>
</section>

<section class="card card--back">
  <div class="brand-name">WRT</div>
  <div class="divider"></div>
  <div class="contact">
    <div class="contact__name">DANIEL REEVES</div>
    <div class="contact__role">Director</div>
    <ul class="contact__list">
      <li>
        <svg viewBox="0 0 16 16" aria-hidden="true"><path d="M3.5 1.5l2.5 3-1.5 1.8c.9 2 2.4 3.5 4.2 4.3L10.5 9l3 2.5-1.3 2.6C7 13.8 2.2 9 1.9 3z" fill="var(--red)"/></svg>
        000 444 000
      </li>
      <li>
        <svg viewBox="0 0 16 16" aria-hidden="true"><rect x="1" y="3" width="14" height="10" fill="var(--red)"/><path d="M1 3.5l7 5 7-5" stroke="#0b0b0b" stroke-width="1.4" fill="none"/></svg>
        email@wrtservices.com.au
      </li>
      <li>
        <svg viewBox="0 0 16 16" aria-hidden="true"><circle cx="8" cy="8" r="7" fill="var(--red)"/><path d="M1 8h14M8 1c-3 3.5-3 10.5 0 14M8 1c3 3.5 3 10.5 0 14" stroke="#0b0b0b" stroke-width="1" fill="none"/></svg>
        www.websiteaddress.com
      </li>
    </ul>
  </div>
  <p class="depot"><span class="depot__label">Depot:</span> Lot 444 example address Australia</p>
</section>

</body>
</html>
```